I need a business card for myself, being a proprietor of a funeral parlor based in Manila. I'd like the card to have either of the following:
White Font on Black Background
or
Black Font on White Background
No logo is needed however I will appreciate any efforts to show a symbol of eternal happiness, aptly designed with above mentioned colors in mind.
Company name, address and contact on the lower right corner.
Logo or symbol anywhere.
Brightvale Funeral Services
+639174412870
dariel4412@quillmail.com
corner of Corvina Avenue and Halberd Street
Makati City, Philippines
Thank you.
Update: Please include a small dove in your design. You are free to choose where you would like it on the card.

```html
<!DOCTYPE html>
<html lang="en">
<head>
<meta charset="utf-8">
<title>Brightvale Funeral Services – Business Card</title>
<link rel="stylesheet" href="https://fonts.googleapis.com/css2?family=Marcellus&family=Lato:wght@400;700&family=PT+Sans+Narrow&display=swap">
<style>
  :root {
    --frame: #000000;
    --card-center: #252825;
    --card-mid: #161816;
    --card-edge: #0b0b0b;
    --ink: #ffffff;
  }
  * { margin: 0; padding: 0; box-sizing: border-box; }
  html, body {
    width: 1200px;
    height: 686px;
    overflow: hidden;
    background: var(--frame);
  }
  .card {
    position: relative;
    width: 1200px;
    height: 686px;
    background: var(--frame);
    padding: 19px;
  }
  .card-face {
    position: relative;
    width: 100%;
    height: 100%;
    background: radial-gradient(ellipse 70% 80% at 52% 45%, var(--card-center) 0%, var(--card-mid) 55%, var(--card-edge) 100%);
    color: var(--ink);
  }
  .brand-name {
    position: absolute;
    left: 43px;
    top: 54px;
    font-family: "Marcellus", serif;
    font-size: 94px;
    line-height: 1;
    letter-spacing: 1px;
    font-weight: 400;
  }
  .brand-tagline {
    position: absolute;
    left: 44px;
    top: 157px;
    font-family: "Lato", sans-serif;
    font-weight: 400;
    font-size: 43px;
    line-height: 1;
    letter-spacing: 14px;
  }
  .brand-mark {
    position: absolute;
    left: 295px;
    top: 222px;
    width: 134px;
    display: flex;
    flex-direction: column;
    align-items: center;
    gap: 12px;
  }
  .brand-mark-circle {
    width: 90px;
    height: 90px;
    border-radius: 50%;
    border: 2px solid var(--ink);
  }
  .brand-mark-name {
    font-family: "Marcellus", serif;
    font-size: 22px;
    line-height: 1;
    letter-spacing: 1px;
  }
  .contact {
    position: absolute;
    left: 658px;
    top: 374px;
    font-family: "PT Sans Narrow", sans-serif;
    font-size: 33px;
    line-height: 38px;
  }
  .contact-phone {
    margin-top: 24px;
    display: flex;
    align-items: center;
    gap: 2px;
    font-family: "Lato", sans-serif;
    font-weight: 700;
    font-size: 33px;
    letter-spacing: 2px;
  }
  .contact-phone svg { width: 30px; height: 30px; }
  .contact-email { margin-top: 8px; font-size: 32px; }
</style>
</head>
<body>
  <div class="card">
    <div class="card-face">
      <h1 class="brand-name">BRIGHTVALE</h1>
      <p class="brand-tagline">FUNERAL SERVICES</p>

      <div class="brand-mark">
        <span class="brand-mark-circle" aria-hidden="true"></span>
        <span class="brand-mark-name">BRIGHTVALE</span>
      </div>

      <div class="contact">
        <p class="contact-address">Corvina Avenue corner Halberd Street<br>Makati City, Philippines</p>
        <p class="contact-phone">
          <svg viewBox="0 0 24 24" aria-hidden="true">
            <circle cx="12" cy="12" r="10.5" fill="none" stroke="#fff" stroke-width="2"/>
            <path d="M9 6.5c-1.5 1-2 3-1 5.5s3 4.8 5.5 5.8c1 .4 2 .2 2.6-.6l.6-.9-2.2-1.6-1 .9c-1.2-.5-2.6-2-3.1-3.2l.9-1-1.4-2.3z" fill="#fff"/>
          </svg>
          +639174412870
        </p>
        <p class="contact-email">dariel4412@quillmail.com</p>
      </div>
    </div>
  </div>
</body>
</html>
```